Construction Company Needs Letterhead Design

We recently had a new logo designed and would like to have our letterhead updated to a trendier design. We are a concrete construction company based out of Iowa, but do work for Agricultural businesses across the Midwest.

Industry/Entity Type

Construction

Colors
ec1f27
000000
ffffff

Requirements
Must have
• Must stay within our current color scheme of red/black/white. Must have have our address, phone number, e-mail address, etc. printed on the letterhead as well.

```html
<!DOCTYPE html>
<html lang="en">
<head>
<meta charset="utf-8">
<title>Harvell Field Works Letterhead</title>
<link rel="stylesheet" href="https://fonts.googleapis.com/css2?family=Open+Sans:wght@400;600;700&display=swap">
<style>
  :root {
    --red: #ec1f27;
    --black: #1a1a1a;
    --white: #ffffff;
    --ink: #2b2b2b;
    --body: #6a6a6a;
    --backdrop: #d1d2d4;
  }
  html, body {
    margin: 0;
    width: 1200px;
    height: 1200px;
    overflow: hidden;
    background: var(--backdrop);
    font-family: "Open Sans", sans-serif;
  }
  .letterhead {
    position: absolute;
    left: 276px;
    top: 112px;
    width: 646px;
    height: 912px;
    background: var(--white);
    box-shadow: 0 6px 14px rgba(0,0,0,0.12);
    overflow: hidden;
  }
  .edge-stripes {
    position: absolute;
    left: 0;
    top: 0;
    width: 24px;
    height: 912px;
  }
  .brand {
    position: absolute;
    top: 64px;
    left: 0;
    width: 100%;
    display: flex;
    justify-content: center;
    align-items: center;
    gap: 8px;
  }
  .brand-mark {
    width: 26px;
    height: 26px;
    background: var(--red);
  }
  .brand-name {
    font-size: 24px;
    font-weight: 700;
    color: var(--black);
    letter-spacing: 0.5px;
  }
  .address {
    position: absolute;
    top: 109px;
    width: 100%;
    text-align: center;
    font-size: 7.5px;
    color: var(--ink);
  }
  .recipient {
    position: absolute;
    left: 102px;
    top: 170px;
    color: var(--ink);
  }
  .recipient .salutation {
    font-size: 10.5px;
    font-weight: 700;
  }
  .recipient .blank {
    display: inline-block;
    width: 62px;
    border-bottom: 1px solid var(--ink);
  }
  .recipient .role {
    font-size: 7px;
    margin-top: 1px;
  }
  .recipient .company {
    font-size: 7.5px;
    font-weight: 700;
    margin-top: 3px;
  }
  .date {
    position: absolute;
    right: 87px;
    top: 175px;
    font-size: 7.5px;
    font-weight: 700;
    color: var(--ink);
  }
  .letter-body {
    position: absolute;
    left: 102px;
    top: 245px;
    width: 466px;
    font-size: 10.2px;
    line-height: 13px;
    color: var(--body);
    text-align: justify;
  }
  .letter-body p {
    margin: 0 0 11px;
  }
  .letter-body p.lead {
    font-weight: 700;
    color: #555;
    margin-bottom: 14px;
  }
  .signature-area {
    position: absolute;
    left: 104px;
    top: 678px;
    width: 96px;
    height: 26px;
    background: linear-gradient(90deg, #e9e9e9, #f4f4f4);
  }
  .signer {
    position: absolute;
    left: 105px;
    top: 717px;
  }
  .signer .name {
    font-size: 13px;
    font-weight: 700;
    color: var(--red);
    letter-spacing: 0.4px;
  }
  .signer .role {
    font-size: 10px;
    color: var(--ink);
    margin-top: 1px;
  }
  .contact-row {
    position: absolute;
    top: 831px;
    left: 94px;
    display: flex;
  }
  .contact-item {
    width: 118px;
    display: flex;
    flex-direction: column;
    align-items: center;
    gap: 11px;
    font-size: 7.5px;
    color: var(--ink);
  }
  .contact-item svg {
    width: 18px;
    height: 20px;
  }
</style>
</head>
<body>
  <main class="letterhead">
    <svg class="edge-stripes" viewBox="0 0 24 912" aria-hidden="true">
      <polygon points="0,182 10,198 10,912 0,912" fill="var(--red)"/>
      <polygon points="10,232 19,248 19,912 10,912" fill="var(--black)"/>
    </svg>

    <header>
      <div class="brand">
        <span class="brand-mark"></span>
        <span class="brand-name">HARVELL FIELD WORKS</span>
      </div>
      <div class="address">18 Millbrook Rd. Ames, IA 50010</div>
    </header>

    <section class="recipient">
      <div class="salutation">Dear, Mr<span class="blank"></span></div>
      <div class="role">Designation</div>
      <div class="company">COMPANY NAME</div>
    </section>
    <div class="date">DATE:08/02/2018</div>

    <article class="letter-body">
      <p>Lorem Ipsum is simply dummy text of the printing and typesetting industry. Lorem Ipsum has been the industry's standard dummy text ever since the 1500s,when an unknown printer took a galley of type and scrambled it to make a type specimen book. It has survived not only five centuries, but also the leap into electronic typesetting, remaining essentially unchanged. It was popularised in the 1960s with the release of Letraset sheets containing Lorem Ipsum passages,and more recently with desktop publishing software like Aldus PageMaker including versions of Lorem Ipsum.</p>
      <p class="lead">Lorem Ipsum is simply dummy text of the printing and typesetting industry. Lorem Ipsum has been the industry's standard dummy text ever since the 1500s,when an unknown printer took a galley of type and scrambled it to make a type specimen book.</p>
      <p>Lorem Ipsum is simply dummy text of the printing and typesetting industry. Lorem Ipsum has been the industry's standard dummy text ever since the 1500s,when an unknown printer took a galley of type and scrambled it to make a type specimen book. It has survived not only five centuries, but also the leap into electronic typesetting, remaining essentially unchanged. It was popularised in the 1960s with the release of Letraset sheets containing Lorem Ipsum passages,and more recently with desktop publishing software like Aldus PageMaker including versions of Lorem Ipsum.It was popularised in the 1960s with the release of Letraset sheets containing Lorem Ipsum passages,and more recently with desktop publishing software like Aldus PageMaker including versions of Lorem Ipsum.</p>
      <p>Lorem Ipsum is simply dummy text of the printing and typesetting industry. Lorem Ipsum has been the industry's standard dummy text ever since the 1500s,when an unknown printer took a galley of type and scrambled it to make a type specimen book. It has survived not only five centuries, but also the leap into electronic typesetting, remaining essentially unchanged. It was popularised in the 1960s with the release of Letraset sheets containing Lorem Ipsum passages,and more recently with desktop publishing software like Aldus PageMaker including versions of Lorem Ipsum.</p>
    </article>

    <div class="signature-area" role="img" aria-label="Handwritten signature"></div>
    <section class="signer">
      <div class="name">YOUR NAME</div>
      <div class="role">Designation</div>
    </section>

    <footer class="contact-row">
      <div class="contact-item">
        <svg viewBox="0 0 18 20" aria-hidden="true">
          <polygon points="9,0 18,5 18,15 9,20 0,15 0,5" fill="var(--red)"/>
          <path d="M6.2 6.2 L7.6 5.8 L8.4 7.6 L7.5 8.4 Q8.3 10.6 10.2 11.6 L11 10.7 L12.8 11.5 L12.4 12.9 Q8.2 13.6 6.2 6.2 Z" fill="var(--white)"/>
        </svg>
        <span>+123-456-7899</span>
      </div>
      <div class="contact-item">
        <svg viewBox="0 0 18 20" aria-hidden="true">
          <polygon points="9,0 18,5 18,15 9,20 0,15 0,5" fill="var(--red)"/>
          <rect x="6.5" y="6" width="5" height="2.5" fill="var(--white)"/>
          <rect x="5" y="8.5" width="8" height="3.5" rx="0.5" fill="var(--white)"/>
          <rect x="6.5" y="11" width="5" height="3" fill="var(--white)" stroke="var(--red)" stroke-width="0.6"/>
        </svg>
        <span>+123-456-7899</span>
      </div>
      <div class="contact-item">
        <svg viewBox="0 0 18 20" aria-hidden="true">
          <polygon points="9,0 18,5 18,15 9,20 0,15 0,5" fill="var(--red)"/>
          <rect x="5" y="7" width="8" height="6" fill="var(--white)"/>
          <path d="M5 7 L9 10.3 L13 7" fill="none" stroke="var(--red)" stroke-width="0.8"/>
        </svg>
        <span>info@harvellfield.com</span>
      </div>
      <div class="contact-item">
        <svg viewBox="0 0 18 20" aria-hidden="true">
          <polygon points="9,0 18,5 18,15 9,20 0,15 0,5" fill="var(--red)"/>
          <circle cx="9" cy="10" r="3.8" fill="none" stroke="var(--white)" stroke-width="1"/>
          <ellipse cx="9" cy="10" rx="1.6" ry="3.8" fill="none" stroke="var(--white)" stroke-width="0.8"/>
          <line x1="5.2" y1="10" x2="12.8" y2="10" stroke="var(--white)" stroke-width="0.8"/>
        </svg>
        <span>www.harvellfield.com</span>
      </div>
    </footer>
  </main>
</body>
</html>
```